Web Design Project for a Software & Consulting Company

We have just completed a recent ArtHive project for a new logo (see attached).
As the next stage of our rebranding we now require a website re-design to complement the new logo.
Our current site, http://www.corvanisoft.com was built in-house and does not come across as professional as we would like. We supply software and associated services to some of the world’s largest oil companies and we need our site to reflect that level of client.
We will also be posting another design project for brochures, PowerPoint slides and other materials very soon.
We would like designs for…
Home page
Product page
• JTP
• LBV
• SGF
Services
News page
About Us page
Contact Us page
Page for mobile devices that gives basic company and product information
Currently the site is small but we intend to increase content to include white papers etc. this should be taken into account when designing the navigation therefore we would prefer navigation through styled text links rather than images.
Colour schemes should broadly be taken from our new logo, where the dark blue and dark green from the left and right sides of the logo are the main colours, but other, brighter accent colours can be used to highlight sections or content.
Dark Blue = C:88, M:55, Y:44, K:28
Dark Green = C:87, M:53, Y:50, K:50
NB: Don’t use the logo on our current site, make sure you use the one attached.
We would prefer the final file format to be a layered PSD.
The site should be clean and professional and communicate the following...
• That we have a great depth and breadth of knowledge about our customers’ business, enabling us to deliver the best systems and solutions.
• That we are a leading provider of cost estimation and control solutions to the oil and gas industry.
• The benefits of our software and consulting services.
• Show that we deliver outstanding customer service and value with a very high level of professionalism
• The site should have no Flash and be able to self-adjust to fit any screen size.
Things to avoid …
• Obvious and clichéd oil industry imagery, no oil rigs
• Cartoon style graphics
Our Background
We are an integrated software and consulting organization specialising in the drilling side of the oil and gas industry. Simply put our software helps companies better understand, predict and communicate the cost of drilling wells.
We have 3 software products and a consulting offering consisting of…
• JTP - Probabilistic time and cost software
• LBV – Cost tracking and reporting software
• SGF – (currently known as TrailMemo) – Lessons learned software
• Consulting services
Our systems are in use in over 30 countries with a broad range of clients including: QZ, Dunmara, Pilk, Ravenor, FELO Curvasti, VASTIRO and Quarlix.
Our current site can be found at www.corvanisoft.com
Our main competitors are
• http://www.lumbrok.com/
• http://www.vantiquo.com/
• http://www.ktv.com/services/software-solutions/z4-
Our depth of drilling knowledge, quality of software and collaboration with clients differentiate us form the competition.
We strive for very high levels of customer service.
We look forward to receiving your designs!
Updates
Thanks to all the designers who have submitted a design, we appreciate the effort.
We will do our best to give individual feedback on each design but given that many are quite similar we thought we would give some general feedback first.
Nearly all the designs submitted so far have been slight variations on…
-
Top Menu
-
Scrolling Photo Banner
-
4 Columns
-
Body
-
Deep Footer
These designs are well executed but they are basically the same layout as our existing site and while there is nothing inherently wrong with this layout we would like to see some designs that are a bit more innovative and different. We don’t really want just a polished version of our current site.
Thanks again,
CVS
Thanks to everyone who has submitted a design, the response has been great.
We are close to making a decision so if you are intending to submit a design please do it soon, the deadline is only a few days away.
Thanks again.
CVS
Target Market(s)
Mid to high level executives
Industry/Entity Type
Oil And Gas
Look and feel

```html
<!DOCTYPE html>
<html lang="en">
<head>
<meta charset="utf-8">
<title>Corvani Soft – Home</title>
<link rel="stylesheet" href="https://fonts.googleapis.com/css2?family=Ubuntu:wght@400;500;700&family=Josefin+Slab:wght@300;400;600&display=swap">
<style>
  :root {
    --page-bg: #123e47;
    --card-bg: #ffffff;
    --teal: #1b6e7e;
    --teal-dark: #0f4f5c;
    --teal-light: #2a8a9c;
    --nav-active: #4c6a14;
    --green: #6a9a16;
    --green-dark: #4f7d0c;
    --band: #e9e9e9;
    --text: #555555;
    --text-dark: #222222;
    --line: #dddddd;
    --white: #ffffff;
  }
  * { box-sizing: border-box; margin: 0; padding: 0; }
  html, body { width: 1000px; height: 1200px; overflow: hidden; }
  body { background: var(--page-bg); font-family: "Ubuntu", sans-serif; color: var(--text); position: relative; }
  .page-card { position: absolute; left: 118px; top: 18px; width: 768px; height: 1002px; background: var(--card-bg); border-radius: 4px; box-shadow: 0 2px 8px rgba(0,0,0,.35); overflow: hidden; }
  .site-header { position: absolute; left: 0; top: 0; width: 768px; height: 109px; border-bottom: 1px solid var(--line); }
  .brand { position: absolute; left: 16px; top: 38px; display: flex; align-items: center; gap: 10px; }
  .brand-mark { width: 34px; height: 34px; border-radius: 50%; background: var(--teal); }
  .brand-name { font-size: 26px; font-weight: 700; color: var(--teal-dark); letter-spacing: .5px; }
  .main-nav { position: absolute; right: 14px; top: 48px; display: flex; font-size: 13px; font-weight: 500; letter-spacing: .3px; }
  .main-nav a { color: var(--teal-dark); text-decoration: none; padding: 0 10px; border-left: 1px solid #e3e3e3; }
  .main-nav a:first-child { border-left: none; }
  .main-nav a.active { color: var(--nav-active); }
  .hero { position: absolute; left: 16px; top: 125px; width: 737px; height: 327px; border-radius: 0 0 34px 0; background: linear-gradient(90deg, #5a8a10 0%, #6b9a16 45%, #5f8f10 100%); overflow: hidden; }
  .hero-visual { position: absolute; left: 40px; top: 0; width: 300px; height: 327px; background: radial-gradient(ellipse at center, #7fae3a 0%, #5b8a16 70%, transparent 100%); }
  .hero-copy { position: absolute; left: 310px; top: 82px; width: 420px; text-align: center; color: var(--white); font-family: "Josefin Slab", serif; line-height: 1; }
  .hero-copy .light { font-weight: 300; font-size: 31px; display: block; }
  .hero-copy .big { font-weight: 400; font-size: 38px; display: block; margin: 8px 0; }
  .hero-copy .mid { font-weight: 300; font-size: 28px; display: block; }
  .news-bar { position: absolute; left: 16px; top: 460px; width: 737px; height: 39px; border: 1px solid var(--line); border-radius: 3px; display: flex; align-items: center; font-size: 11px; }
  .news-label { display: flex; align-items: center; gap: 10px; padding: 0 14px 0 8px; height: 100%; border-right: 1px solid var(--line); color: var(--teal); font-size: 14px; font-weight: 500; }
  .news-text { padding-left: 12px; color: var(--text); flex: 1; }
  .news-text b { color: var(--text-dark); font-weight: 500; }
  .news-more { color: var(--teal-light); padding-right: 16px; }
  .process-band { position: absolute; left: 0; top: 510px; width: 768px; height: 240px; background: linear-gradient(#e6e6e6, #f4f4f4 60%, #ffffff); }
  .step { position: absolute; top: 0; width: 176px; }
  .step-title { height: 42px; line-height: 40px; text-align: center; font-size: 20px; color: var(--text-dark); }
  .step-card { background: linear-gradient(#ffffff, #f1f1f1); border: 1px solid #e0e0e0; border-radius: 3px; height: 187px; box-shadow: 0 2px 3px rgba(0,0,0,.06); position: relative; }
  .step-head { height: 33px; line-height: 31px; padding-left: 9px; color: var(--white); font-size: 13px; font-weight: 500; background: linear-gradient(var(--teal-light), var(--teal-dark)); border-radius: 3px 3px 0 0; }
  .step-body { padding: 12px 9px 0; font-size: 11.5px; line-height: 16px; color: var(--text); }
  .read-more { position: absolute; left: 12px; right: 12px; bottom: 9px; height: 26px; line-height: 26px; padding-left: 8px; background: #e4e4e4; border-radius: 3px; font-size: 11.5px; font-weight: 500; color: var(--teal-dark); }
  .read-more::after { content: ""; position: absolute; right: 9px; top: 9px; border-left: 5px solid var(--teal-dark); border-top: 4px solid transparent; border-bottom: 4px solid transparent; }
  .flow-arrow { position: absolute; top: 8px; }
  .about { position: absolute; left: 16px; top: 764px; width: 740px; }
  .about h2 { font-size: 24px; font-weight: 500; color: var(--teal); margin-bottom: 9px; }
  .about p { font-size: 11.5px; line-height: 14px; margin-bottom: 8px; }
  .clients-tab { position: absolute; left: 318px; top: 888px; width: 132px; height: 30px; background: var(--band); border-radius: 12px 12px 0 0; text-align: center; line-height: 32px; font-size: 19px; color: var(--text-dark); }
  .clients { position: absolute; left: 0; top: 916px; width: 768px; height: 86px; background: var(--band); display: flex; align-items: center; justify-content: space-between; padding: 0 18px; }
  .client { font-size: 14px; font-weight: 700; color: #3f5a60; }
  .site-footer { position: absolute; left: 118px; top: 1040px; width: 770px; color: var(--white); font-size: 11px; }
  .office { position: absolute; top: 0; width: 180px; }
  .office h3 { font-size: 19px; font-weight: 500; margin-bottom: 14px; }
  .contact-row { position: relative; padding-left: 25px; line-height: 14px; margin-bottom: 12px; }
  .contact-row svg { position: absolute; left: 0; top: 0; }
  .partner-badge { position: absolute; left: 640px; top: 8px; width: 36px; height: 36px; background: #4fa3b0; border-radius: 6px; }
  .social { position: absolute; left: 707px; top: 93px; display: flex; gap: 5px; }
  .social span { width: 28px; height: 28px; border-radius: 5px; background: #9a9fa1; }
  .copyright { position: absolute; right: 0; top: 131px; }
</style>
</head>
<body>
  <div class="page-card">
    <header class="site-header">
      <div class="brand"><span class="brand-mark"></span><span class="brand-name">CORVANI SOFT</span></div>
      <nav class="main-nav">
        <a class="active" href="#">HOME</a><a href="#">PRODUCT</a><a href="#">SERVICES</a><a href="#">NEWS</a><a href="#">ABOUT US</a><a href="#">CONTACT US</a>
      </nav>
    </header>

    <section class="hero">
      <div class="hero-visual" role="img" aria-label="Green leaves surrounding a white wall socket with a green plug"></div>
      <div class="hero-copy">
        <span class="light">TrailMemo</span>
        <span class="big">LESSONS LEARNED</span>
        <span class="mid">for the</span>
        <span class="big">OIL &amp; GAS INDUSTRY.</span>
      </div>
    </section>

    <div class="news-bar">
      <div class="news-label">
        <svg width="20" height="17" viewBox="0 0 20 17"><rect x="3" y="1" width="16" height="15" fill="none" stroke="#333" stroke-width="1.6"/><rect x="1" y="5" width="3" height="11" fill="none" stroke="#333" stroke-width="1.4"/><path d="M6 5h10M6 8h10M6 11h10M6 14h6" stroke="#333" stroke-width="1.4"/></svg>
        Latest News
      </div>
      <div class="news-text"><b>JTP Selected by Norvel Gastrans</b> Norvel Gastrans E &amp; P GmbH has selected JTP as the solution...</div>
      <div class="news-more">Morer news</div>
    </div>

    <section class="process-band">
      <svg class="flow-arrow" style="left:164px" width="76" height="26" viewBox="0 0 76 26"><path d="M4 22 Q38 0 70 18" fill="none" stroke="#b5b5b5" stroke-width="2"/><path d="M62 16l9 3-4-9" fill="none" stroke="#b5b5b5" stroke-width="2"/></svg>
      <svg class="flow-arrow" style="left:346px" width="76" height="26" viewBox="0 0 76 26"><path d="M4 22 Q38 0 70 18" fill="none" stroke="#b5b5b5" stroke-width="2"/><path d="M62 16l9 3-4-9" fill="none" stroke="#b5b5b5" stroke-width="2"/></svg>
      <svg class="flow-arrow" style="left:537px" width="76" height="26" viewBox="0 0 76 26"><path d="M4 22 Q38 0 70 18" fill="none" stroke="#b5b5b5" stroke-width="2"/><path d="M62 16l9 3-4-9" fill="none" stroke="#b5b5b5" stroke-width="2"/></svg>

      <div class="step" style="left:16px">
        <div class="step-title" style="text-align:left;padding-left:66px">Plan</div>
        <div class="step-card"><div class="step-head">Time &amp; Cost Estimation</div>
          <p class="step-body">JTP delivers a standardized, systematic approach to understanding, quantifying and communicating the impact of project risk to all stakeholders.</p>
          <div class="read-more">Read More</div></div>
      </div>
      <div class="step" style="left:201px">
        <div class="step-title">Execute</div>
        <div class="step-card"><div class="step-head">Materials &amp; Cost Control</div>
          <p class="step-body">Since 1992 LBV has been helping companies optimize their materials and logistics processes and accurately track costs on a daily basis.</p>
          <div class="read-more">Read More</div></div>
      </div>
      <div class="step" style="left:389px">
        <div class="step-title">Learn</div>
        <div class="step-card"><div class="step-head">Lessons Learned</div>
          <p class="step-body">TrailMemo is an advanced lessons learned and knowledge management system for use in the Oil &amp; Gas industry. It's fully searchable and easy to use.</p>
          <div class="read-more">Read More</div></div>
      </div>
      <div class="step" style="left:576px">
        <div class="step-title" style="text-align:right;padding-right:52px">Embed</div>
        <div class="step-card"><div class="step-head">Services &amp; Consulting</div>
          <p class="step-body">Software solutions rely on people and processes to deliver results. From analysis through execution we support our clients to improve performance.</p>
          <div class="read-more">Read More</div></div>
      </div>
    </section>

    <section class="about">
      <h2>A Bit About Us</h2>
      <p>Corvani Soft have developed and continue to support software in over 30 countries, providing real results to hundreds of drilling operations.</p>
      <p>With decades of hands-on software and well engineering experience, we are uniquely positioned to provide the right solution to our customers.</p>
    </section>

    <div class="clients-tab">Our Clients</div>
    <section class="clients">
      <span class="client">Pilk</span>
      <span class="client">Dunmara</span>
      <span class="client">FELO</span>
      <span class="client">VASTIRO</span>
      <span class="client">Tarnly</span>
      <span class="client">Brenholt</span>
      <span class="client">Maravel</span>
      <span class="client">Ravenor</span>
      <span class="client">QZ</span>
    </section>
  </div>

  <footer class="site-footer">
    <div class="office" style="left:0">
      <h3>Europe</h3>
      <div class="contact-row"><svg width="14" height="18" viewBox="0 0 14 18"><path d="M7 17C2 10 1 8 1 6a6 6 0 0 1 12 0c0 2-1 4-6 11z" fill="#4f8f9a"/><circle cx="7" cy="6" r="2.2" fill="#123e47"/></svg>18 Harlow Lane<br>Westbury, WB4 2KD</div>
      <div class="contact-row"><svg width="12" height="18" viewBox="0 0 12 18"><rect x="2" y="1" width="8" height="15" rx="1.5" fill="#4f8f9a"/><rect x="3.5" y="3" width="5" height="8" fill="#123e47"/></svg>Phone:<br>+44(0)1632 960418</div>
      <div class="contact-row"><svg width="16" height="12" viewBox="0 0 16 12"><rect x="1" y="2" width="14" height="9" fill="#4f8f9a"/><path d="M1 2l7 5 7-5" fill="none" stroke="#123e47" stroke-width="1.2"/></svg>Email:<br>eu@corvanisoft.com</div>
    </div>
    <div class="office" style="left:187px">
      <h3>North America</h3>
      <div class="contact-row"><svg width="14" height="18" viewBox="0 0 14 18"><path d="M7 17C2 10 1 8 1 6a6 6 0 0 1 12 0c0 2-1 4-6 11z" fill="#4f8f9a"/><circle cx="7" cy="6" r="2.2" fill="#123e47"/></svg>1200 Parkline Drive, Suite 410<br>Brookfield, TX 77500</div>
      <div class="contact-row"><svg width="12" height="18" viewBox="0 0 12 18"><rect x="2" y="1" width="8" height="15" rx="1.5" fill="#4f8f9a"/><rect x="3.5" y="3" width="5" height="8" fill="#123e47"/></svg>Phone:<br>(555) 014 2278</div>
      <div class="contact-row"><svg width="16" height="12" viewBox="0 0 16 12"><rect x="1" y="2" width="14" height="9" fill="#4f8f9a"/><path d="M1 2l7 5 7-5" fill="none" stroke="#123e47" stroke-width="1.2"/></svg>Email:<br>us@corvanisoft.com</div>
    </div>
    <div class="partner-badge" role="img" aria-label="Software partner badge"></div>
    <div class="social" aria-label="Social links"><span></span><span></span></div>
    <div class="copyright">© 2013 Corvani Soft</div>
  </footer>
</body>
</html>
```